Dental Office Needs- Flyer Design for Same Day Crowns

We need a flyer that will explain the benefits of the same day crown from the patient prospective. Not show pictures of the machine that makes the crowns. See attached material for content. The flyer should use the practices PMS colors of Green 562 and Blue 3025. The ad should say to the patient - I want to go this office and get my crown done there.
Updates

Project Deadline Extended Reason: The difference in the time zone between USA and Europe has caused issues. Minor changes still need to be worked out. Added Thursday, July 14, 2016

Target Market(s)

Dental Patients

Industry/Entity Type

Dental

Requirements
Must have
• Call to Action
• Business Address and Business Logo
• Classic Design
• images of a Happy 50 year old Couple
• Gives the benefits of the same day crown
Should not have
• No Images of tooth figures
• No before or after pictures

```html
<!DOCTYPE html>
<html lang="en">
<head>
<meta charset="utf-8">
<title>Harbor Lane Dental – Same-Day Crown Flyer</title>
<link href="https://fonts.googleapis.com/css2?family=Play&family=Playfair+Display&family=Marcellus&family=Roboto:wght@400&display=swap" rel="stylesheet">
<style>
  :root{
    --green:#21915a;
    --blue:#0a4a63;
    --white:#ffffff;
    --paper:#fdfefe;
    --photo-light:#eef3f1;
    --photo-pink:#e9cfd8;
    --photo-mint:#bfe3cf;
  }
  *{margin:0;padding:0;box-sizing:border-box}
  html,body{width:1200px;height:1200px;overflow:hidden;background:var(--white)}
  .canvas{position:relative;width:1200px;height:1200px;background:var(--white)}
  .panel{position:absolute;top:202px;height:795px;width:375px;overflow:hidden}
  .panel--benefits{left:38px;background:var(--green);color:var(--white);text-align:center;font-family:"Play",sans-serif}
  .benefits__headline{position:absolute;top:52px;left:0;right:0;font-size:28px;line-height:55.5px;letter-spacing:.5px}
  .benefits__list{position:absolute;top:393px;left:0;right:0;list-style:none;font-size:18.5px;line-height:34.8px}
  .benefits__curve{position:absolute;left:0;bottom:0;width:375px;height:80px}
  .panel--question{left:413px;background:var(--paper)}
  .question__block{position:absolute;top:0;left:0;width:375px;height:538px;background:var(--blue)}
  .question__text{position:absolute;top:194px;left:0;right:0;text-align:center;color:var(--white);font-family:"Playfair Display",serif;font-size:23px;line-height:50.5px;transform:scaleX(.86)}
  .question__rule{position:absolute;top:531px;left:48px;width:280px;height:2px;background:linear-gradient(90deg,transparent,#cfe3ea,transparent)}
  .brand{position:absolute;left:0;right:0;text-align:center;font-family:"Marcellus",serif;color:var(--blue);font-size:35px;white-space:nowrap}
  .brand__dot{display:inline-block;width:14px;height:14px;border-radius:50%;background:var(--green);margin-right:10px;vertical-align:middle}
  .panel--question .brand{top:628px}
  .panel--cover{left:787px;background:var(--white)}
  .panel--cover .brand{top:130px;font-size:33px}
  .farewell{position:absolute;top:233px;left:0;right:0;list-style:none;text-align:center;font-family:"Roboto",sans-serif;color:var(--blue);font-size:15px;line-height:39.5px;letter-spacing:.2px}
  .couple-photo{position:absolute;left:21px;top:350px;width:354px;height:445px;background:
     radial-gradient(ellipse at 30% 55%,var(--photo-pink),transparent 60%),
     radial-gradient(ellipse at 80% 70%,var(--photo-mint),transparent 60%),
     var(--photo-light)}
</style>
</head>
<body>
<main class="canvas">
  <section class="panel panel--benefits">
    <h1 class="benefits__headline" style="font-weight:400">When it comes<br>to your next crown,<br>the benefits of a<br>Digital Restoration<br>add up quickly!</h1>
    <ul class="benefits__list">
      <li>A Same-Day</li><li>Restoration</li><li>+</li>
      <li>A Stronger</li><li>More Precise Fit</li><li>+</li>
      <li>A Beautiful</li><li>Natural Appearance</li>
    </ul>
    <svg class="benefits__curve" viewBox="0 0 375 80" preserveAspectRatio="none" aria-hidden="true">
      <path d="M0 80 L0 44 Q187 -38 375 44 L375 80 Z" fill="#0a4a63"/>
      <path d="M30 33 Q187 -22 345 33" fill="none" stroke="#ffffff" stroke-width="3"/>
    </svg>
  </section>

  <section class="panel panel--question">
    <div class="question__block">
      <p class="question__text">Are you ready for a dramatically<br>improved experience with your<br>next crown?</p>
    </div>
    <div class="question__rule"></div>
    <p class="brand"><span class="brand__dot"></span>Harbor Lane Dental</p>
  </section>

  <section class="panel panel--cover">
    <p class="brand"><span class="brand__dot"></span>Harbor Lane Dental</p>
    <ul class="farewell">
      <li>GOOD-BYE TEMPORARY CROWN</li>
      <li>GOOD-BYE SECOND APPOINTMENT</li>
      <li>GOOD-BYE GOOEY MESSY IMPRESSIONS</li>
    </ul>
    <div class="couple-photo" role="img" aria-label="Photo of a smiling couple in their fifties embracing"></div>
  </section>
</main>
</body>
</html>
```